Logo and *CLEAR* creative Business Card

Looking for a creative transparent business card design for a custom clothing printing business for Businesses, Bands and Sportsteams; we will also be selling other promotional items, but our main focus is on t-shirts. The business name is Larkfield Apparel, and we are looking for something to make us stand out.

Will need a logo included. Must be easy to read, include a T-shirt somewhere in the logo or business card design, since that is our main focus, and we want that to be very clear. Logo should look good as a standalone logo, if the t-shirt were to be removed later, so the text is important.

Card should be credit card sized (slightly different than standard paper business cards): 85.5mm x 54mm. Needs 1.5mm bleed around edges.

Can be clear or frosted.

AI Vector file is best, or high quality 600+ dpi file.
Will require separate file of the logo, which should be large, or scalable.

Looking for something bold and modern. Hopefully something creative, and outside the box. Please see Look and Feel sliders.

We want the shape of a t-shirt, but it could be made to look metallic, glossy like shiny glass or plastic, a mosiac, or globs/brushes/splatter of paint. Each side of the shirt could be a different color if you want... We just want something that doesn't look like clip art of a typical t-shirt.
Updates

In case you missed it, I have changed the sliders, as well as a few details in the ad.  I have also added new pictures of examples for inspiration. 

One thing that is important to note, is the QR barcode, should not be transparent, since I worry that people will try to scan it from the wrong side, or it will be hard to scan depending on what is behind the card.

Please do not simply copy a logo from the attached files.  They are for inspiration only, and would need to at least be altered before being used. 

I like the idea of making a t-shirt prominent in the business card design, maybe working it into the background, or into certain elements within it.

Thanks,

Dale.

 

Feel Free to do something unconventional and creative, playing with shapes or negative space within the layout.  Darker designs might work, as well as text with depth/shine/3d look.

**Please notice I have increased the budget of this project to make it worth the while of artists to raise the quality of the designs. 

I have updated the attached files, and included comments and suggestions for various ideas that could be used in business card designs. 

Included in these files, is a picture of hole punch options, which can be included in your designs.  It allows for a regular round hole punch, as well as an irregular longer version. 

Please also note that corners can be round or square. 

If you follow the recommendations, I'm sure you will end up with a good looking design.

Thanks,

Dale.

Reason: I feel like some designers need a little more time and then i can decide on fully developed designs.

Reason: Just looking for some requested alterations from my top choices

Target Market(s)

Would like to appeal to a wide variety of people: Business owners/managers, Sports teams, and Bands are our customers (in order of importance).

Industry/Entity Type

Credit Card

Requirements
Must have
• **T-shirt in design or logo or both**
- Modern
- Wide Appeal (appeal to educated 25 - 50 year olds)
- A QR barcode to scan to add contact info to someone's phone(we will supply barcode) with brief explanation of the barcode ("Add contact info: [%]")Barcode should not be over transparent background, which may make it difficult to scan, or could be scanned from the wrong side of the card.
- Name: Dale Wexcott
- Position: Owner
- Business Name: Larkfield Apparel
- Ph: (supplied on completion)
- e-mail address: ""
- facebook page:""

**Will not include an address or fax number**

-Under the Name, it should say "Custom T-Shirts, etc" or "T-Shirt Printing, etc."

Nice to have
• Since the business card is either clear or frosted transparent, I would like the amount of words that can be seen (backwards) from the otherside, kept to a minimum.

- A subtle amount of foil print would be nice.

- Would like to see examples that are CREATIVE, possibly involving the tshirt, so right away someone knows what the company is all about.

Can also include a slogan such as "Your Brand is Our Business"

Design Detail is appreciated! :) Possibly something unconventional.

-Hole punch somewhere in the design. See attached file.
Should not have
• - comic sans, or other over used/cliche fonts.

- Should not be too hard to read.

-

```html
<!DOCTYPE html>
<html lang="en">
<head>
<meta charset="utf-8">
<title>Larkfield Apparel – Business Card</title>
<link rel="stylesheet" href="https://fonts.googleapis.com/css2?family=Montserrat:wght@500;600;700;800&display=swap">
<style>
  :root {
    --backdrop: #dfe2e6;
    --frost-top: rgba(255, 255, 255, 0.78);
    --frost-bottom: rgba(236, 241, 245, 0.70);
    --card-edge: rgba(255, 255, 255, 0.95);
    --card-inner: rgba(255, 255, 255, 0.55);
    --ink: #111214;
    --ink-soft: #2b2d30;
    --brand-red: #c10d0d;
  }
  * { box-sizing: border-box; margin: 0; padding: 0; }
  html, body {
    width: 1200px;
    height: 1200px;
    overflow: hidden;
    background: var(--backdrop);
    font-family: "Montserrat", sans-serif;
    color: var(--ink);
  }
  .canvas {
    position: relative;
    width: 1200px;
    height: 1200px;
  }
  .card {
    position: absolute;
    left: 80px;
    top: 317px;
    width: 1040px;
    height: 566px;
    background: linear-gradient(160deg, var(--frost-top) 0%, rgba(250,252,253,0.74) 50%, var(--frost-bottom) 100%);
    border: 2px solid var(--card-edge);
    box-shadow: 0 18px 40px rgba(40, 48, 60, 0.14), inset 0 0 0 6px var(--card-inner);
  }
  .brand {
    position: absolute;
    left: 52px;
    top: 61px;
    width: 371px;
    height: 375px;
    display: flex;
    flex-direction: column;
    align-items: center;
    justify-content: center;
    gap: 24px;
  }
  .brand-mark {
    width: 72px;
    height: 72px;
    background: var(--brand-red);
  }
  .brand-name {
    font-weight: 800;
    font-size: 58px;
    line-height: 1.04;
    text-align: center;
    color: var(--brand-red);
    text-transform: uppercase;
  }
  .tagline {
    position: absolute;
    left: 52px;
    top: 458px;
    width: 371px;
    text-align: center;
    font-weight: 700;
    color: var(--ink);
  }
  .tagline-top {
    display: block;
    font-size: 16px;
    letter-spacing: 7px;
  }
  .tagline-bottom {
    display: block;
    margin-top: 4px;
    font-size: 28px;
    line-height: 34px;
    letter-spacing: 10px;
  }
  .person {
    position: absolute;
    top: 214px;
    left: 446px;
    width: 320px;
    text-align: center;
  }
  .person-name {
    font-weight: 700;
    font-size: 33px;
    color: var(--ink);
  }
  .person-role {
    margin-top: 6px;
    font-weight: 600;
    font-size: 13px;
    letter-spacing: 3px;
    color: var(--ink-soft);
  }
  .details {
    position: absolute;
    top: 368px;
    left: 474px;
    font-weight: 600;
    font-size: 21px;
    color: var(--ink);
  }
  .details-line { display: block; line-height: 36px; }
  .phone {
    position: absolute;
    top: 468px;
    left: 440px;
    display: flex;
    align-items: center;
    gap: 16px;
    font-weight: 700;
    font-size: 31px;
  }
  .phone-icon { width: 36px; height: 36px; }
</style>
</head>
<body>
<main class="canvas">
  <section class="card">
    <div class="brand">
      <span class="brand-mark" aria-hidden="true"></span>
      <span class="brand-name">Larkfield<br>Apparel</span>
    </div>
    <p class="tagline">
      <span class="tagline-top">CUSTOM T-SHIRT</span>
      <span class="tagline-bottom">PRINTING</span>
    </p>
    <div class="person">
      <p class="person-name">Dale Wexcott</p>
      <p class="person-role">OWNER</p>
    </div>
    <div class="details">
      <span class="details-line">dale@larkfieldapparel.com</span>
      <span class="details-line">facebook.com/larkfieldapparel</span>
    </div>
    <p class="phone">
      <svg class="phone-icon" viewBox="0 0 36 36" aria-hidden="true">
        <circle cx="18" cy="18" r="15" fill="none" stroke="#111214" stroke-width="2.5"/>
        <path d="M12 10 l4 -1 2 5 -2.5 2 q2 4 5.5 6 l2 -2.5 5 2 -1 4 q-9 1 -15 -15z" fill="#111214"/>
      </svg>
      <span>0800 555 0142</span>
    </p>
  </section>
</main>
</body>
</html>
```